Classical Chamber Choir needs an electronic and printable flyer for an Easter Concert

I am the new Artistic Director of the Varlow Singers. We would like to advertise our upcoming concert on April 5 and are seeking a new, more youthful, contemporary look for the choir's advertising. Previously they have used classical curly letters and dark colours. Perhaps black/grey and white would work?
The choir is 27 years old and has many loyal and some quite elderly singers. We would now like to extend our appeal to the younger singers who are in the choir - age group 35 - 60 and we are keen to attract more in the 30/40 age group. I would like something contemporary in feel, uncluttered, minimalist and artistically appealing. More Wolanitz than Durac - more Lorvasini than Halvick. Some inspiration starters: Tedrilo line drawings, linocut designs, Ivor Hadcombe pencil drawings. I am hoping these references might inspire you. Here are some other ideas using line from Dénes Halkó:
https://photos.web.vlx.io/mT4pLwRyh82BnWcaQ
https://photos.web.vlx.io/3HRnVkTaWpDcuLe48
We would require an A4 flyer, (high res. and low res.) DL, jpg for Gridwave and a 10cm. size to put on the front of the Concert Programme.

```html
<!DOCTYPE html>
<html lang="en">
<head>
<meta charset="utf-8">
<title>Varlow Singers – Halmer at Easter</title>
<link href="https://fonts.googleapis.com/css2?family=Jost:wght@400;500;600&family=League+Spartan:wght@600;700;800&display=swap" rel="stylesheet">
<style>
  :root {
    --paper: #ffffff;
    --ink: #000000;
    --slate: #444b4c;
    --frame: #a9abab;
    --panel-light: #bccaca;
    --panel-dark: #a3afaf;
    --title-tint: #bfcece;
    --forest: #1f5a4d;
    --lime: #f1fb6a;
    --white: #ffffff;
    --muted: #a8a8a8;
  }
  * { margin: 0; padding: 0; box-sizing: border-box; }
  html, body { width: 848px; height: 1200px; overflow: hidden; background: var(--paper); }
  .flyer {
    position: relative; width: 848px; height: 1200px; overflow: hidden;
    font-family: "Jost", sans-serif; background: var(--paper);
  }
  .line {
    position: absolute; left: 0; width: 848px; text-align: center;
    line-height: 1; white-space: nowrap;
  }
  .presenter { top: 28px; font-size: 54px; font-weight: 400; color: var(--slate); letter-spacing: 2px; left: -8px; }
  .frame { position: absolute; left: 51px; top: 98px; width: 730px; height: 1021px; border: 2px solid var(--frame); }
  .headline {
    top: 104px; left: -8px; font-family: "League Spartan", sans-serif; font-weight: 700;
    font-size: 78px; color: var(--title-tint); letter-spacing: 3px;
  }
  .panel {
    position: absolute; left: 60px; top: 159px; width: 712px; height: 892px;
    background: linear-gradient(160deg, var(--panel-light) 0%, var(--panel-light) 45%, var(--panel-dark) 100%);
  }
  .church-sketch {
    position: absolute; left: 60px; top: 550px; width: 712px; height: 501px;
    background: linear-gradient(180deg, rgba(163,175,175,0) 0%, rgba(140,152,152,0.35) 60%, rgba(130,142,142,0.45) 100%);
  }
  .text-block { position: absolute; left: -8px; top: 0; width: 848px; height: 1200px; }
  .work { top: 172px; font-size: 38px; font-weight: 500; color: var(--white); letter-spacing: 1px; }
  .company { top: 209px; font-size: 29px; font-weight: 500; color: var(--forest); letter-spacing: 0.5px; }
  .masters { top: 250px; font-size: 39px; font-weight: 500; color: var(--ink); letter-spacing: 1px; }
  .composers { top: 298px; font-family: "League Spartan", sans-serif; font-size: 31px; font-weight: 800; color: var(--white); }
  .venue { font-family: "League Spartan", sans-serif; font-size: 50px; font-weight: 800; color: var(--forest); }
  .venue-1 { top: 357px; }
  .venue-2 { top: 402px; }
  .street { top: 453px; font-size: 29px; font-weight: 600; color: var(--forest); letter-spacing: 0.5px; }
  .date { top: 490px; font-size: 58px; font-weight: 600; color: var(--lime); }
  .label { font-size: 26px; font-weight: 600; color: var(--ink); }
  .label-soloists { top: 571px; }
  .label-men-1 { top: 675px; }
  .label-quartet { top: 727px; }
  .label-men-2 { top: 835px; }
  .names { font-family: "League Spartan", sans-serif; font-size: 32px; font-weight: 800; color: var(--white); }
  .names-a { top: 606px; }
  .names-b { top: 640px; }
  .names-c { top: 766px; }
  .names-d { top: 800px; }
  .accompanist { top: 877px; }
  .director-role { top: 932px; font-size: 29px; font-weight: 600; color: var(--lime); }
  .director-name { top: 960px; font-family: "League Spartan", sans-serif; font-size: 48px; font-weight: 800; color: var(--lime); }
  .tickets {
    position: absolute; left: 60px; top: 1051px; width: 712px; height: 62px;
    background: var(--ink); color: var(--white); font-size: 26px; font-weight: 500;
    display: flex; align-items: center; justify-content: center; white-space: nowrap;
  }
  .programmes {
    position: absolute; right: 67px; top: 1126px; font-size: 18px; font-weight: 500;
    color: var(--muted); letter-spacing: 0.8px; line-height: 1;
  }
</style>
</head>
<body>
<main class="flyer">
  <p class="line presenter">VARLOW SINGERS PRESENT</p>
  <div class="frame"></div>
  <h1 class="line headline">HALMER AT EASTER</h1>
  <div class="panel"></div>
  <div class="church-sketch" role="img" aria-label="Loose pencil line sketch of a small stone church with a steep gable, cross and rose window"></div>
  <div class="text-block">
    <p class="line work">HALMER STABAT MATER H 214</p>
    <p class="line company">in the company of the</p>
    <p class="line masters">RUSSIAN MASTERS</p>
    <p class="line composers">VETRENKOV, SORIN, DUBROVALOV, LESNIKOV</p>
    <p class="line venue venue-1">ST BRENDAN MARNE</p>
    <p class="line venue venue-2">CHURCH</p>
    <p class="line street">CORVELL STREET ASHBY RIDGE</p>
    <p class="line date">5PM APRIL 5 2020</p>
    <p class="line label label-soloists">SOLOISTS</p>
    <p class="line names names-a">LENA HARTWICK, ADRIAN COLVANE,</p>
    <p class="line names names-b">GERALD FENMORE</p>
    <p class="line label label-men-1">TENOR LINE</p>
    <p class="line label label-quartet">STRING QUARTET</p>
    <p class="line names names-c">YURI PASHENKO, MIRA TEOH,</p>
    <p class="line names names-d">ROWAN DELBY, FERENC TÁLLYAI</p>
    <p class="line label label-men-2">TENOR LINE</p>
    <p class="line names accompanist">JULIET ORMSBY</p>
    <p class="line director-role">ARTISTIC DIRECTOR</p>
    <p class="line director-name">ILONA VERESMARTY</p>
  </div>
  <div class="tickets">Tickets $30/ $25/ $10 Student/ Children under 12 free</div>
  <p class="programmes">PROGRAMMES: GOLD COIN DONATION</p>
</main>
</body>
</html>
```